Labels for fruit liqueur bottles

We are looking for a visual identity based on our logo, for fruit liqueur labels. To date, we have different liqueurs such as: lemon liqueur, orange liqueurs, mandarin liqueurs, grapefruit liqueurs. We will then create other liqueurs such as strawberry, apple or even apricot. Our goal is to have a single visual that we can adapt in different colors depending on the fruit used.

On the label there should be:
the logo
homemade
the name of the fruit (which can be changed depending on the product)
swiss-made
50cl
21°

Colors

Designer to choose colors to be used in the design.

Requirements
Must have
• a visual of liquor bottle labels, with the possibility of changing the background colors, depending on the fruit used
Nice to have
• something modern and nice to look at. We must be able to read the basic fruit in the blink of an eye. it is also possible to have a black or white or colored label background.

```html
<!DOCTYPE html>
<html lang="en">
<head>
<meta charset="utf-8">
<title>Casa Vellino – Lemon liqueur labels</title>
<link rel="stylesheet" href="https://fonts.googleapis.com/css2?family=Arimo:wght@400;700&family=Barlow:wght@400;500&display=swap">
<style>
  :root {
    --bg: #ffffff;
    --band: #161616;
    --strip: #262626;
    --brand-orange: #ec5a24;
    --fruit-yellow: #e4d81c;
    --fruit-light: #b9cf44;
    --ink: #1e1e1e;
    --swiss-red: #e2231a;
    --rule: #d9d5d2;
  }
  * { margin: 0; padding: 0; box-sizing: border-box; }
  html, body { width: 1200px; height: 1200px; overflow: hidden; background: var(--bg); }
  .canvas { position: relative; width: 1200px; height: 1200px; }

  .neck-label { position: absolute; left: 0; top: 0; }
  .neck-name { font-family: "Arimo", Arial, sans-serif; font-weight: 700; font-size: 25px; fill: #ffffff; }
  .neck-tag { font-family: "Arimo", Arial, sans-serif; font-weight: 700; font-size: 11px; fill: var(--fruit-yellow); letter-spacing: 0.5px; }

  .front-label {
    position: absolute; left: 585px; top: 546px; width: 330px; height: 412px;
    background: var(--bg); box-shadow: 0 0 0 1px #eeeeee;
    display: flex; flex-direction: column; align-items: center;
  }
  .brand { margin-top: 22px; display: flex; flex-direction: column; align-items: center; }
  .brand-dot { width: 30px; height: 30px; border-radius: 50%; background: var(--brand-orange); margin-bottom: 8px; }
  .brand-name { font-family: "Arimo", Arial, sans-serif; font-weight: 700; font-size: 17px; color: var(--brand-orange); letter-spacing: -0.2px; line-height: 1; }
  .brand-tag { font-family: "Arimo", Arial, sans-serif; font-weight: 700; font-size: 7.5px; color: var(--brand-orange); margin-top: 2px; letter-spacing: 0.4px; }

  .kind { margin-top: 32px; font-family: "Barlow", sans-serif; font-weight: 400; font-size: 28px; color: var(--fruit-light); letter-spacing: 1px; line-height: 1; }
  .fruit { margin-top: 8px; font-family: "Barlow", sans-serif; font-weight: 500; font-size: 70px; color: var(--fruit-yellow); letter-spacing: 3px; line-height: 1; }
  .wave { margin-top: 8px; }

  .origin { margin-top: 38px; display: flex; align-items: center; gap: 10px; font-family: "Barlow", sans-serif; font-size: 21px; color: var(--ink); letter-spacing: 0.6px; }
  .swiss-flag { width: 18px; height: 18px; }

  .rule { position: absolute; left: 0; right: 0; top: 350px; height: 10px; background: linear-gradient(var(--rule), #f2f0ee); }
  .specs {
    position: absolute; left: 0; right: 0; bottom: 0; height: 52px; background: var(--band);
    display: flex; align-items: center; justify-content: center; gap: 14px;
    font-family: "Barlow", sans-serif; font-size: 24px; color: #ffffff; letter-spacing: 2px;
  }
  .specs-divider { width: 3px; height: 24px; background: var(--fruit-yellow); }
</style>
</head>
<body>
<div class="canvas">

  <svg class="neck-label" width="1200" height="1200" viewBox="0 0 1200 1200" aria-label="Neck label strip">
    <rect x="320" y="221" width="74" height="699" rx="37" fill="var(--strip)"/>
    <circle cx="357" cy="570" r="75" fill="var(--strip)"/>
    <circle cx="357" cy="570" r="36" fill="var(--brand-orange)"/>
    <g transform="translate(345,278) rotate(90)">
      <text class="neck-name" x="0" y="0" textLength="206" lengthAdjust="spacingAndGlyphs">CASA VELLINO</text>
      <text class="neck-tag" x="0" y="16">liqueur de fruits</text>
    </g>
    <g transform="translate(366,864) rotate(-90)">
      <text class="neck-name" x="0" y="0" textLength="206" lengthAdjust="spacingAndGlyphs">CASA VELLINO</text>
      <text class="neck-tag" x="0" y="13">liqueur de fruits</text>
    </g>
  </svg>

  <section class="front-label">
    <div class="brand">
      <div class="brand-dot"></div>
      <div class="brand-name">CASA VELLINO</div>
      <div class="brand-tag">liqueur de fruits</div>
    </div>
    <div class="kind">Homemade</div>
    <div class="fruit">LEMON</div>
    <svg class="wave" width="48" height="8" viewBox="0 0 48 8">
      <path d="M2 4 q5 -4 9 0 t9 0 t9 0 t9 0 t9 0" fill="none" stroke="var(--fruit-yellow)" stroke-width="2" stroke-linecap="round"/>
    </svg>
    <div class="origin">
      <svg class="swiss-flag" viewBox="0 0 18 18">
        <rect width="18" height="18" fill="var(--swiss-red)"/>
        <rect x="7.5" y="3.5" width="3" height="11" fill="#fff"/>
        <rect x="3.5" y="7.5" width="11" height="3" fill="#fff"/>
      </svg>
      <span>swiss-made</span>
    </div>
    <div class="rule"></div>
    <div class="specs">
      <span>21°</span>
      <span class="specs-divider"></span>
      <span>50cl</span>
    </div>
  </section>

</div>
</body>
</html>
```